Flyer for an online formula one racing league

Hello.

I am looking for the perfect one page facebook/instagram style flyer for an online formula one racing league. The racing league is called 'VOLTA RACING LEAGUE'.

Information that MUST be on the new flyer is already on the old flyer I have uploaded here. In addition to including: The Volta racing league 'V' logo I have uploaded AND the text: 'Very popular, clean and competitive racing league, running for its 4th season. Why not join with a friend? Race times, Mondays, Tuesdays and Wednesdays each at 8pm UK TIME Message below for any questions. (Spacing of information is not important, however all the information in regards to the racing I have just mentioned MUST BE on the flyer, this includes info from old pic, logo and the other info I just mentioned).

It would be beneficial to have lots of dark blue on the flyer and the new flyer to be a lot different to the original flyer I uploaded, but this is not essential.

I apologise if I did not explain very well, any questions, please message me.

The best flyer should look the most attractive to someone that might be interested in joining an online formula one racing league.

I used this website before to create the perfect logo for my Sunday League team last year, and I was very impressed. I look forward to seeing your submissions.

Target Market(s)

No specific target, more something that may attract someone into joining a formula one online racing league

Industry/Entity Type

e sports/formula one

Colors
0054AA
0677BA
7BADD7
CADEEF
E8F1F8

Requirements
Must have
• Read product description please
Should not have
• Ignoring product description!

```html
<!DOCTYPE html>
<html lang="en">
<head>
<meta charset="utf-8">
<title>Volta Racing League – New Season</title>
<link href="https://fonts.googleapis.com/css2?family=Orbitron:wght@800&family=Poppins:ital,wght@0,400;0,600;0,700;1,500;1,600&display=swap" rel="stylesheet">
<style>
  :root {
    --navy-deep: #0a1a6e;
    --navy: #12278f;
    --logo-disc: #0b0f3a;
    --pill-blue: #1f3cff;
    --pill-accent: #e8357e;
    --white: #ffffff;
    --soft-blue: #cadeef;
    --gold: #f7c317;
    --flag-light: #d9d9d9;
    --flag-dark: #3a3a3a;
  }
  * { margin: 0; padding: 0; box-sizing: border-box; }
  html, body { width: 1200px; height: 630px; overflow: hidden; }
  body { font-family: "Poppins", sans-serif; color: var(--white); }

  .flyer {
    position: relative;
    width: 1200px;
    height: 630px;
    overflow: hidden;
    background: radial-gradient(ellipse at 50% 45%, var(--navy) 0%, var(--navy-deep) 100%);
  }

  .track-texture {
    position: absolute;
    inset: 0;
    background: radial-gradient(circle at 20% 80%, rgba(255,255,255,0.04), transparent 60%),
                radial-gradient(circle at 85% 20%, rgba(255,255,255,0.04), transparent 55%);
  }

  .flag {
    position: absolute;
    top: 35px;
    width: 150px;
    height: 140px;
    border-radius: 12px;
    background: linear-gradient(135deg, var(--flag-light), var(--flag-dark));
    opacity: 0.9;
  }
  .flag--left { left: 345px; transform: rotate(-8deg); }
  .flag--right { left: 705px; transform: rotate(8deg); }

  .brand-mark {
    position: absolute;
    left: 500px;
    top: 15px;
    width: 200px;
    height: 200px;
    border-radius: 50%;
    background: var(--logo-disc);
    display: flex;
    align-items: center;
    justify-content: center;
  }
  .brand-mark__name {
    font-family: "Orbitron", sans-serif;
    font-weight: 800;
    font-size: 30px;
    color: var(--white);
    letter-spacing: 2px;
  }

  .league-title {
    position: absolute;
    top: 208px;
    width: 100%;
    text-align: center;
    font-family: "Orbitron", sans-serif;
    font-size: 42px;
    font-weight: 800;
    letter-spacing: 3px;
    line-height: 1.2;
  }

  .year-pill {
    position: absolute;
    left: 431px;
    top: 280px;
    width: 338px;
    height: 40px;
    border-radius: 20px;
    background: var(--pill-blue);
    box-shadow: 4px 4px 0 var(--pill-accent);
    display: flex;
    align-items: center;
    justify-content: center;
    font-style: italic;
    font-weight: 500;
    font-size: 22px;
  }

  .info {
    position: absolute;
    width: 100%;
    text-align: center;
    line-height: 1.25;
  }
  .info--schedule { top: 336px; font-size: 30px; font-weight: 700; }
  .info--season { top: 386px; font-size: 37px; font-weight: 700; color: var(--gold); }
  .info--clean { top: 435px; font-size: 36px; font-weight: 700; }
  .info--divisions { top: 484px; font-size: 31px; font-weight: 400; }
  .info--popular { top: 532px; font-size: 21px; font-weight: 600; color: var(--soft-blue); }
  .info--contact { top: 574px; font-size: 20px; font-weight: 600; font-style: italic; color: var(--gold); }
</style>
</head>
<body>
  <main class="flyer">
    <div class="track-texture" role="img" aria-label="Faint tyre track pattern across the background"></div>

    <div class="flag flag--left" role="img" aria-label="Chequered racing flag on a pole"></div>
    <div class="flag flag--right" role="img" aria-label="Chequered racing flag on a pole"></div>

    <div class="brand-mark">
      <span class="brand-mark__name">VOLTA</span>
    </div>

    <h1 class="league-title">VOLTA RACING LEAGUE</h1>

    <div class="year-pill">Running for its 4th season</div>

    <p class="info info--schedule">Mondays, Tuesdays and Wednesdays each at 8pm UK TIME</p>
    <p class="info info--season">New season just starting!!!</p>
    <p class="info info--clean">Clean Online Racing League</p>
    <p class="info info--divisions">3 divisions currently and looking to keep growing!</p>
    <p class="info info--popular">Very popular, clean and competitive racing league. Why not join with a friend?</p>
    <p class="info info--contact">Feel free to message us below for any inquiries!</p>
  </main>
</body>
</html>
```